Dental Business Card

I need Dental oriented business cards.
On the front side -
- on the first line, my name:
Dr Marlow Tasker
- on the second line (just underneath):
Doctor of Dental Medicine
- on the third line, or underneath that or in a corner, I would like the address and phone number:
5192 Ch. Birchfield
Montreal QC H2P 4K8
514-629-5074
- other than that i would maybe like a logo of a tooth, but i want it to be subtle and very basic!
- I would like the card to be preferably black or dark grey-ish with the writing in white
On the other side -
- 2-3 lines with the possibility to write the next appointment the box with the lines should be white, with the rest of the card being black

```html
<!DOCTYPE html>
<html lang="en">
<head>
<meta charset="utf-8">
<title>Tasker Dental – Business Card</title>
<link rel="stylesheet" href="https://fonts.googleapis.com/css2?family=Open+Sans:wght@400;600;700&display=swap">
<style>
  :root {
    --backdrop: #3b3c3f;
    --card: #050505;
    --card-glow: #1c1c1c;
    --swirl: #161616;
    --ink: #ffffff;
    --ink-soft: #bdbdbd;
    --rule: #333333;
    --panel: #ffffff;
  }
  html, body {
    margin: 0;
    width: 1200px;
    height: 900px;
    overflow: hidden;
    background: var(--backdrop);
    font-family: "Open Sans", sans-serif;
  }
  .sheet {
    width: 1200px;
    height: 900px;
    display: flex;
    flex-direction: column;
    align-items: center;
    justify-content: center;
    gap: 40px;
  }
  .card {
    position: relative;
    width: 630px;
    height: 360px;
    background: radial-gradient(circle at 45% 40%, var(--card-glow), var(--card) 65%);
    overflow: hidden;
    box-shadow: 0 14px 30px rgba(0,0,0,0.45);
  }
  .swirl {
    position: absolute;
    right: 0;
    bottom: 0;
    width: 360px;
    height: 230px;
  }
  /* Front */
  .brand {
    position: absolute;
    left: 60px;
    top: 80px;
    color: var(--ink-soft);
    font-size: 17px;
    font-weight: 600;
    letter-spacing: 0.5px;
  }
  .identity {
    position: absolute;
    left: 50px;
    top: 150px;
    width: 300px;
    color: var(--ink);
  }
  .identity .name {
    margin: 0;
    font-size: 27px;
    font-weight: 700;
    line-height: 1.2;
    white-space: nowrap;
  }
  .identity .title {
    margin: 10px 0 0;
    font-size: 19px;
    font-weight: 600;
    white-space: nowrap;
  }
  .divider {
    position: absolute;
    left: 378px;
    top: 60px;
    width: 2px;
    height: 200px;
    background: linear-gradient(to bottom, rgba(255,255,255,0.05), rgba(255,255,255,0.7) 50%, rgba(255,255,255,0.05));
  }
  .contact {
    position: absolute;
    left: 402px;
    top: 80px;
    color: var(--ink);
    font-size: 15px;
    line-height: 1.35;
    white-space: nowrap;
  }
  .contact-row {
    display: flex;
    align-items: flex-start;
    gap: 12px;
    margin-bottom: 22px;
  }
  .contact-row svg { flex: none; margin-top: 2px; }
  /* Back */
  .back .brand {
    left: 0;
    right: 0;
    top: 34px;
    text-align: center;
    font-size: 14px;
  }
  .appointment {
    position: absolute;
    left: 110px;
    top: 70px;
    width: 410px;
    height: 210px;
    background: var(--panel);
    box-sizing: border-box;
    padding: 50px 36px 0;
  }
  .appointment .line {
    height: 1px;
    background: var(--rule);
    margin-bottom: 52px;
  }
</style>
</head>
<body>
<main class="sheet">
  <section class="card back" aria-label="Card back – appointment">
    <svg class="swirl" viewBox="0 0 360 230" aria-hidden="true">
      <path d="M40 230 C20 150 90 110 170 130 C240 150 260 90 330 40 L360 30 L360 230 Z" fill="var(--swirl)"/>
    </svg>
    <div class="brand">Tasker Dental</div>
    <div class="appointment">
      <div class="line"></div>
      <div class="line"></div>
      <div class="line"></div>
    </div>
  </section>

  <section class="card front" aria-label="Card front – contact">
    <svg class="swirl" viewBox="0 0 360 230" aria-hidden="true">
      <path d="M60 230 C30 160 100 120 180 140 C250 160 270 100 340 50 L360 40 L360 230 Z" fill="var(--swirl)"/>
    </svg>
    <div class="brand">Tasker Dental</div>
    <div class="identity">
      <h1 class="name">Dr. MARLOW TASKER</h1>
      <p class="title">Doctor of Dental Medicine</p>
    </div>
    <div class="divider"></div>
    <div class="contact">
      <div class="contact-row">
        <svg width="20" height="24" viewBox="0 0 20 24" aria-hidden="true">
          <path d="M10 1.5 C5 1.5 2 5 2 9 C2 14 10 22 10 22 C10 22 18 14 18 9 C18 5 15 1.5 10 1.5 Z" fill="none" stroke="#fff" stroke-width="1.6"/>
          <circle cx="10" cy="9" r="3" fill="none" stroke="#fff" stroke-width="1.6"/>
        </svg>
        <div>5192 Ch. Birchfield<br>Montreal QC H2P 4K8</div>
      </div>
      <div class="contact-row">
        <svg width="20" height="20" viewBox="0 0 20 20" aria-hidden="true">
          <circle cx="10" cy="10" r="8.5" fill="none" stroke="#fff" stroke-width="1.6"/>
          <path d="M7 6 L8.5 6 L9 8 L8 9 C8.6 10.3 9.7 11.4 11 12 L12 11 L14 11.5 L14 13 C10 13.5 6.5 10 7 6 Z" fill="#fff"/>
        </svg>
        <div>514-629-5074</div>
      </div>
    </div>
  </section>
</main>
</body>
</html>
```